My name is Tomas Verenda, and I have done business with your company several times. I need a business card to represent my business, I own a company by the name of BELOMI Suntan Lotion & Sunscreen.
My requirements are as follow: My company logo in the brightest gold possible, on a black, grainy (sandy) background, with shading around the each element. With the company name in gold, a stylized coconut trees, and some type of wave graphic in gold. "A product of the USA, Cedar Hollow, NY"
"For comments, suggestion, or ordering please contact us at:
belomi42@nexamail.test"

"BELOMI™ Tanning Lotion & Sunscreen―Crafted with Care"

Belomi Tanning Lotion & Sunscreen is the most extraordinary and innovative sun tanning product to emerge in several generations. The constituents of this product are formidable substances that protect the skin against the aftermath of sun exposure−before you exposed yourself to the sun’s rays. The Aloe Vera in this product, along with other oils and cream, are specifically manufactured to lessen the symptoms of extended exposure to the sun. Belomi is designed to provide a Broad Spectrum Protection (50) that assist in the reduction of (UVA) and (UVB) radiation to create a magnificent sun-absorbing, long-lasting, deep dark bronzing experience.
Thank you,
Tomas Verenda
tomastverenda@postline.test

Target Market(s)

Sunscreen

Industry/Entity Type

Business

Contact Information for Business Card

BELOMI™ Tanning Lotion and Sunscreen
Crafted with Care

Belomi Tanning Lotion is the most extraordinary and innovative sun tanning product to emerge in several generations. The constituents of this product are formidable substances that protect the skin against the aftermath of sun exposure−before you exposed yourself to the sun’s rays. The Aloe Vera, in this product, along with other oils and cream, are specifically manufactured to lessen the symptoms of extended exposure to the sun. Belomi protects your skin from dehydration and treat your skin with the products we apply to ourselves after a sunburn−before the sun tanning process begins. Belomi is designed to provide a Broad Spectrum Protection (50) that assist in the reduction of (UVA) and (UVB) radiation to create a magnificent sun-absorbing, long-lasting, deep dark bronzing experience.

Colors
fece3e
acd136

Requirements
Must have
• Black Card Stock with grainy surface, Gold Logo, stylized Coconut Palm Tree, Company Name, email address, and NYC location.
• Modern Layout with Modern fonts and graphics

```html
<!DOCTYPE html>
<html lang="en">
<head>
<meta charset="utf-8">
<title>BELOMI Suntan Lotion – Business Card</title>
<link href="https://fonts.googleapis.com/css2?family=Arimo:wght@400;700&display=swap" rel="stylesheet">
<style>
  :root {
    --stage: #2b2520;
    --card-black: #0b0b0b;
    --card-sheen: #1c1c1c;
    --gold: #e2b257;
    --gold-soft: #c99a4e;
    --ink-light: #e9e2d4;
  }
  * { box-sizing: border-box; margin: 0; padding: 0; }
  html, body {
    width: 1200px; height: 858px; overflow: hidden;
    background: var(--stage);
    font-family: "Arimo", Arial, sans-serif;
  }
  .stage {
    width: 1200px; height: 858px;
    display: flex; align-items: center; justify-content: center; gap: 48px;
  }
  .card {
    position: relative;
    width: 540px; height: 310px;
    background: radial-gradient(ellipse at 30% 20%, var(--card-sheen), var(--card-black) 70%);
    border-radius: 4px;
    box-shadow: 0 14px 30px rgba(0,0,0,.55);
    overflow: hidden;
  }
  .brand { display: flex; align-items: center; gap: 16px; }
  .brand-dot { border-radius: 50%; background: var(--gold); flex: none; }
  .brand-text { display: flex; flex-direction: column; }
  .brand-name {
    font-weight: 700;
    color: var(--gold);
    letter-spacing: .04em;
    line-height: 1;
  }
  .brand-sub {
    color: var(--gold);
    font-weight: 400;
    letter-spacing: .06em;
    text-transform: uppercase;
    line-height: 1.1;
  }

  /* front */
  .card-front { padding: 34px 44px; }
  .card-front .brand-dot { width: 58px; height: 58px; }
  .card-front .brand-name { font-size: 40px; }
  .card-front .brand-sub { font-size: 15px; margin-top: 4px; }
  .person-name {
    margin: 12px 0 0 74px;
    color: var(--gold-soft);
    font-size: 20px;
  }
  .contact {
    margin-top: 20px;
    color: var(--ink-light);
    font-size: 15px;
    line-height: 1.55;
  }
  .contact .email { font-size: 18px; margin-top: 6px; }

  /* back */
  .card-back {
    display: flex; flex-direction: column; align-items: center; justify-content: center;
  }
  .card-back .brand-dot { width: 96px; height: 96px; }
  .card-back .brand-name { font-size: 60px; }
  .card-back .brand-sub { font-size: 22px; margin-top: 6px; }
  .tagline {
    margin-top: 28px;
    color: var(--ink-light);
    font-size: 14px;
    letter-spacing: .02em;
  }
</style>
</head>
<body>
<main class="stage">
  <section class="card card-front">
    <div class="brand">
      <span class="brand-dot"></span>
      <div class="brand-text">
        <span class="brand-name">BELOMI</span>
        <span class="brand-sub">Suntan Lotion</span>
      </div>
    </div>
    <p class="person-name">Tomas Verenda</p>
    <div class="contact">
      <p>A product of the USA, Cedar Hollow, NY</p>
      <p>For comments, suggestion, or ordering please<br>contact us at:</p>
      <p class="email">belomi42@nexamail.test</p>
    </div>
  </section>

  <section class="card card-back">
    <div class="brand">
      <div class="brand-text">
        <span class="brand-name">BELOMI</span>
        <span class="brand-sub">Suntan Lotion</span>
      </div>
      <span class="brand-dot"></span>
    </div>
    <p class="tagline">BELOMI™ Tanning Lotion &amp; Sunscreen―Crafted with Care</p>
  </section>
</main>
</body>
</html>
```